Medical Company in need of Modern business card design for new Wound Care clinic.

Modern business card design for our Woundcare company. Logo and description of services can be found on our website; https://www.tovrel-woundcare.com/

```html
<!DOCTYPE html>
<html lang="en">
<head>
<meta charset="utf-8">
<title>Tovrel Woundcare – Business Cards</title>
<link rel="stylesheet" href="https://fonts.googleapis.com/css2?family=Open+Sans:wght@400;600;700&family=Montserrat:wght@400&display=swap">
<style>
  :root {
    --backdrop: #222222;
    --card: #ffffff;
    --gold: #c0882a;
    --gold-soft: #f7efe2;
    --ink: #1a1a1a;
  }
  * { margin: 0; padding: 0; box-sizing: border-box; }
  html, body { width: 1200px; height: 780px; overflow: hidden; }
  body {
    background: var(--backdrop);
    font-family: "Open Sans", Arial, sans-serif;
    color: var(--ink);
    position: relative;
  }
  .card {
    position: absolute;
    top: 236px;
    width: 540px;
    height: 308px;
    background: var(--card);
    overflow: hidden;
  }
  .card--front { left: 40px; }
  .card--back { left: 620px; }
  .card__wash {
    position: absolute;
    left: 60px; top: 60px;
    width: 300px; height: 248px;
    background: linear-gradient(135deg, var(--gold-soft) 0%, rgba(247,239,226,0) 70%);
  }
  .card__divider {
    position: absolute;
    left: 0; top: 0;
    width: 540px; height: 308px;
  }
  .brand {
    position: absolute;
    left: 34px; top: 46px;
    display: flex; align-items: center; gap: 10px;
    font-family: "Montserrat", Arial, sans-serif;
    font-weight: 400;
    font-size: 17px;
    letter-spacing: 4px;
  }
  .brand__mark { width: 14px; height: 14px; background: var(--gold); }
  .brand--gold .brand__name { color: var(--gold); }
  .brand--dark .brand__name { color: var(--ink); }

  .person { position: absolute; left: 290px; top: 92px; }
  .person__name { color: var(--gold); font-weight: 700; font-size: 29px; line-height: 1.1; }
  .person__title { font-weight: 600; font-size: 16px; margin-bottom: 14px; }
  .contact-list { list-style: none; }
  .contact-list li { display: flex; align-items: center; gap: 9px; font-size: 14px; line-height: 24px; }
  .contact-list svg { width: 14px; height: 14px; fill: var(--gold); flex: none; }

  .address {
    position: absolute;
    left: 34px; bottom: 26px;
    font-size: 13px;
  }

  .services { position: absolute; left: 290px; top: 70px; width: 230px; }
  .services__heading { color: var(--gold); font-weight: 700; font-size: 16px; margin-bottom: 6px; }
  .services__list { list-style: none; }
  .services__list li {
    position: relative;
    padding-left: 16px;
    font-size: 13px;
    font-weight: 600;
    line-height: 19px;
    margin-bottom: 2px;
  }
  .services__list li::before {
    content: "";
    position: absolute; left: 0; top: 5px;
    width: 8px; height: 8px; border-radius: 50%;
    background: var(--gold);
  }
</style>
</head>
<body>

<section class="card card--front" aria-label="Business card front">
  <div class="card__wash"></div>
  <svg class="card__divider" viewBox="0 0 540 308"><line x1="190" y1="250" x2="270" y2="90" stroke="var(--gold)" stroke-width="1.2"/></svg>
  <div class="brand brand--gold"><span class="brand__mark"></span><span class="brand__name">TOVREL WOUNDCARE</span></div>
  <div class="person">
    <h1 class="person__name">Daniel Varga</h1>
    <p class="person__title">Managing Director</p>
    <ul class="contact-list">
      <li><svg viewBox="0 0 24 24"><path d="M6.6 10.8a15 15 0 0 0 6.6 6.6l2.2-2.2c.3-.3.7-.4 1-.2 1.1.4 2.3.6 3.6.6.6 0 1 .4 1 1V20c0 .6-.4 1-1 1A17 17 0 0 1 3 4c0-.6.4-1 1-1h3.5c.6 0 1 .4 1 1 0 1.3.2 2.5.6 3.6.1.3 0 .7-.2 1z"/></svg>555-210-4187</li>
      <li><svg viewBox="0 0 24 24"><path d="M6 2h9v6H6zM3 9h18v12H3zM6 12v2h3v-2zm5 0v2h3v-2zm5 0v2h2v-2zM6 16v2h3v-2zm5 0v2h3v-2z"/></svg>(555) 309-7724</li>
      <li><svg viewBox="0 0 24 24"><path d="M12 2a10 10 0 1 0 0 20 10 10 0 0 0 0-20zm6.9 6h-3a15 15 0 0 0-1.3-3.9A8 8 0 0 1 18.9 8zM12 4c.8 1.2 1.5 2.5 1.9 4h-3.8c.4-1.5 1.1-2.8 1.9-4zM4.3 14a8 8 0 0 1 0-4h3.4a16 16 0 0 0 0 4zm.8 2h3a15 15 0 0 0 1.3 3.9A8 8 0 0 1 5.1 16zM8.1 8h-3a8 8 0 0 1 4.3-3.9A15 15 0 0 0 8.1 8zM12 20c-.8-1.2-1.5-2.5-1.9-4h3.8c-.4 1.5-1.1 2.8-1.9 4zm2.3-6H9.7a14 14 0 0 1 0-4h4.6a14 14 0 0 1 0 4zm.3 5.9c.6-1.2 1-2.5 1.3-3.9h3a8 8 0 0 1-4.3 3.9zM16.3 14a16 16 0 0 0 0-4h3.4a8 8 0 0 1 0 4z"/></svg>www.tovrel-woundcare.com</li>
      <li><svg viewBox="0 0 24 24"><path d="M3 5h18v14H3zm2 2v.5l7 4.5 7-4.5V7zm0 2.9V17h14V9.9l-7 4.5z"/></svg>info@tovrel-woundcare.com</li>
    </ul>
  </div>
  <p class="address">1820 Alder Ln Ste 200 Springfield, TX 75000</p>
</section>

<section class="card card--back" aria-label="Business card back">
  <div class="card__wash"></div>
  <svg class="card__divider" viewBox="0 0 540 308"><line x1="190" y1="250" x2="270" y2="60" stroke="var(--gold)" stroke-width="1.2"/></svg>
  <div class="brand brand--dark"><span class="brand__mark"></span><span class="brand__name">TOVREL WOUNDCARE</span></div>
  <div class="services">
    <h2 class="services__heading">OUR SERVICES</h2>
    <ul class="services__list">
      <li>Hyperbaric Oxygen Therapy (HBO): A Cornerstone of Advanced Wound Care</li>
      <li>Debridement</li>
      <li>Advanced Wound Dressings</li>
      <li>Bio-engineered Skin Substitutes</li>
      <li>Compression Therapy and Edema Management</li>
    </ul>
  </div>
</section>

</body>
</html>
```